Make the design for the landing page of ReviewCodeHub.com

Laravel is framework (software to build websites)
Goal:
Build a professional landing page to offer free Laravel consultancy sessions in exchange for an email address and to promote your paid services.
🎯 Primary Objective
Convert visitors into leads by offering a free Laravel code audit or strategy session. Capture their email and optionally allow them to directly book a call or hire your services.
🧠 Target Audience
>Companies and startups with Laravel apps
>CTOs and tech leads managing legacy Laravel code
>Freelance developers looking to improve their architecture
>Product owners facing bugs or scaling issues
📐 Suggested Page Structure
1. Hero Section (Top of Page - Above the Fold)
Headline (focused on pain/problem):
“Is your Laravel app slow, outdated or full of bugs?”
Subheadline (clear promise of value):
“Book a free Laravel code audit and get actionable insights in just 30 minutes.”
Primary CTA (email capture form):
Email input
Button: “Schedule Free Consultation”
Secondary CTA Button:
“Free Consultancy” or “Hire My Services”
✅ Make this CTA bold, highly visible, and frictionless
✅ You can use Calendly, TidyCal, or a simple form for scheduling
2. Section: “Are you struggling with any of these?”
Use a vertical scroll experience with checkmarks or icons to highlight common pain points:
🔼 Upgrading PHP / Laravel
🧪 No automated tests
🐛 Recurring bugs
🔐 Security issues
🐢 Slow performance
🧱 Messy architecture or no clear structure
📦 Outdated packages / dependencies
Make this visually engaging — for example, animated list items as the user scrolls down.
3. What You Get With a Free Audit
A personalized code review or system analysis
Architecture & performance insights
No commitment, no spam
+12 years of Laravel experience
Delivered via a video call or written feedback
4. About Me / Why Trust Me
Short section introducing you:
Your experience with Laravel (12+ years)
Notable companies, projects, or logos (if any)
CodeVault / Scribely / Open Source contributions
Maybe include a friendly photo or avatar
5. Call to Action (Repeat CTA)
Reinforce the offer:
“Let’s fix your Laravel headaches together — for free.”
Button: “Book My Free Call”
Optional email input form again (for easy access)
6. Testimonials (Optional but Recommended)
If you already have satisfied clients:
2-3 short quotes with names and roles
Example: “Tobías helped us restructure our legacy Laravel codebase in a week. Highly recommended!”
7. FAQ Section (Optional)
Common questions to eliminate hesitation:
What happens after I submit my email?
Is the consultancy really free?
What kind of projects do you work with?
How long does the call last?
8. Footer
Quick access buttons:
“Schedule Consultation”
“Hire My Services”
Contact email
Linked social profiles or CodeVault
✨ Design Style & Inspirations
Clean, minimalist layout (like craftingbackend.io, but with more obvious CTAs)
Technical yet friendly tone
Use soft animations and icons to break sections
What I would like to see?
An obvious CTA in the middle to the page in order to schedule a 30-mins free consultancy .
also a when you scroll you will see something like
"These problems are common for you"
With the list of common PHP/Laravel problems.
Also would like a button in the top right that says
"Audit me now" like "Get unstuck" in https://craftingbackend.io/
Take inspiration from:
https://craftingbackend.io/
https://www.devguidly.io/
Use this as the logo
https://samplefrosty47.minipage.site/png/logo
Consultancy Project
1 page

```html
<!DOCTYPE html>
<html lang="en">
<head>
<meta charset="utf-8">
<title>ReviewCodeHub – Free Laravel Code Audit</title>
<link href="https://fonts.googleapis.com/css2?family=Lexend:wght@300;400;500;600&display=swap" rel="stylesheet">
<style>
:root{
  --red:#ff2314;
  --red-soft:#ffe3e1;
  --ink:#111111;
  --text:#222222;
  --black:#000000;
  --card:#161616;
  --line:#d9d9d9;
  --white:#ffffff;
}
*{margin:0;padding:0;box-sizing:border-box}
html,body{width:1200px;height:3710px;overflow:hidden;background:var(--white)}
body{font-family:'Lexend',sans-serif;font-weight:300;color:var(--text);position:relative}
.abs{position:absolute}
.red{color:var(--red)}
.btn-outline{position:absolute;border:1.5px solid var(--red);color:var(--red);border-radius:24px;font-size:13px;font-weight:400;text-transform:uppercase;display:flex;align-items:center;justify-content:center}
.btn-solid{position:absolute;background:var(--red);color:var(--white);border-radius:24px;font-size:12px;font-weight:400;text-transform:uppercase;display:flex;align-items:center;justify-content:center}
.brand{position:absolute;background:var(--red-soft);color:var(--red);border-radius:22px;font-size:21px;font-weight:500;display:flex;align-items:center;justify-content:center;gap:8px}
.brand i{width:12px;height:12px;border-radius:50%;background:var(--red);display:block}

/* nav */
.nav{top:0;left:0;width:1200px;height:80px}
.nav-links{left:438px;top:33px;display:flex;gap:30px;font-size:13px;font-weight:400;color:var(--ink);text-transform:uppercase}
.nav-links .active{color:var(--red)}

/* hero */
.hero{left:58px;top:80px;width:1084px;height:476px;border-radius:26px;overflow:hidden;background:linear-gradient(100deg,#f3f3f3 0%,#e6e6e6 50%,#d8d8d8 100%)}
.hero-photo{position:absolute;right:0;top:0;width:640px;height:476px;background:linear-gradient(100deg,rgba(230,230,230,0) 0%,#d6d0ca 30%,#b8a18a 60%,#8f7257 75%,#d9d9d9 100%)}
.hero-blob{position:absolute;right:-30px;top:-40px;width:170px;height:170px;border-radius:50%;background:#f7d9d7}
.hero h1{position:absolute;left:50px;top:78px;font-size:29px;font-weight:500;line-height:51px;color:var(--ink);width:560px}
.hero p{position:absolute;left:53px;top:186px;font-size:15px;line-height:34px;color:var(--ink);width:430px}
.hero-form{position:absolute;left:53px;top:278px;width:420px;height:42px;border-radius:22px;background:var(--white)}
.hero-form span{position:absolute;left:17px;top:14px;font-size:11px;color:#999;text-transform:uppercase}

/* struggling */
.struggle-photo{left:122px;top:642px;width:480px;height:414px;border-radius:22px;background:linear-gradient(135deg,#f1f3f5,#c8d0d6 55%,#8a98a4)}
.struggle-frame{left:134px;top:652px;width:476px;height:410px;border:1.5px solid var(--red);border-radius:22px}
.struggle h2{position:absolute;left:664px;top:646px;font-size:29px;font-weight:500;line-height:48px;color:var(--ink);width:460px}
.checklist{position:absolute;left:663px;top:766px;list-style:none;font-size:15px;color:var(--ink)}
.checklist li{height:41px;display:flex;align-items:center;gap:26px}

/* audit band */
.audit{left:0;top:1148px;width:1200px;height:460px;background:var(--black)}
.audit h2{position:absolute;top:58px;width:1200px;text-align:center;font-size:29px;font-weight:500;color:var(--white)}
.cards{position:absolute;left:110px;top:138px;display:flex;gap:12px}
.card{width:186px;height:249px;background:var(--card);border-radius:8px;color:var(--white);font-size:15px;line-height:35px;text-align:center;display:flex;flex-direction:column;align-items:center;justify-content:center;padding:0 10px}
.card.on{background:var(--red)}
.card svg{margin-bottom:14px}

/* trust */
.trust h2{position:absolute;left:112px;top:1680px;font-size:29px;font-weight:500;color:var(--ink)}
.trust p{position:absolute;left:112px;top:1748px;width:440px;font-size:15px;line-height:34px;color:var(--ink)}
.links{position:absolute;left:112px;top:1900px;list-style:none;font-size:16px;font-weight:400;color:var(--ink)}
.links li{height:50px;display:flex;align-items:center;gap:20px}
.links i{width:22px;height:22px;border-radius:50%;display:block}
.trust-photo{left:672px;top:1692px;width:420px;height:414px;border-radius:22px;background:linear-gradient(160deg,#3e3e3e,#6f6256 45%,#b9a896 80%,#cfc3b6)}
.trust-frame{left:662px;top:1700px;width:418px;height:414px;border:1.5px solid var(--red);border-radius:22px}
.badge{left:680px;top:1898px;width:172px;height:198px;border-radius:18px;background:var(--red);color:var(--white);text-align:center;font-weight:500;font-size:19px;line-height:44px;padding-top:12px}
.badge strong{font-size:30px;font-weight:500;display:block}

/* partners */
.partners{left:112px;top:2175px;display:flex;gap:17px}
.partner{width:181px;height:110px;background:var(--white);box-shadow:0 2px 8px rgba(0,0,0,.08);display:flex;align-items:center;justify-content:center;gap:8px;font-size:16px;font-weight:400;color:#333}
.partner i{width:12px;height:12px;border-radius:50%;background:var(--red);display:block}
.arrow{width:32px;height:32px;border:1.5px solid #222;border-radius:50%;display:flex;align-items:center;justify-content:center}

/* cta band */
.cta{left:0;top:2368px;width:1200px;height:178px;background:var(--black)}
.cta h2{position:absolute;left:111px;top:36px;font-size:29px;font-weight:500;line-height:48px;color:var(--white)}

/* testimonials */
.testi-title{top:2618px;width:1200px;text-align:center;font-size:29px;font-weight:500;color:var(--ink)}
.testi{position:absolute;top:2712px;width:328px;height:328px;padding:16px 18px}
.testi.on{background:#f3f3f3;border:1.5px solid #f1b6b1}
.avatar{width:74px;height:74px;border-radius:50%;background:linear-gradient(135deg,#dfe3e6,#97a3ad)}
.stars{margin-top:26px;color:#f7c531;font-size:15px;letter-spacing:5px}
.testi h3{margin-top:18px;font-size:20px;font-weight:500;color:var(--red)}
.testi p{margin-top:12px;font-size:14px;line-height:33px;color:var(--ink)}

/* faq */
.faq-title{top:3114px;width:1200px;text-align:center;font-size:29px;font-weight:500;color:var(--ink)}
.faq{position:absolute;width:430px;height:58px;border-bottom:1px solid var(--line);font-size:15px;color:var(--ink);display:flex;align-items:center;justify-content:space-between}
.plus{width:16px;height:16px;border:1px solid #333;border-radius:50%;display:flex;align-items:center;justify-content:center;font-size:13px;line-height:1}

/* footer */
.footer{left:0;top:3494px;width:1200px;height:216px;background:var(--black)}
.footer .rule{position:absolute;left:111px;top:140px;width:977px;height:1px;background:#333}
.copy{position:absolute;left:110px;top:178px;font-size:13px;font-weight:400;color:var(--white);text-transform:uppercase}
.socials{position:absolute;left:928px;top:170px;display:flex;gap:7px}
.socials i{width:27px;height:27px;border:1.5px solid var(--white);border-radius:50%;display:block}
.btn-foot{position:absolute;border:1.5px solid var(--red);color:var(--white);border-radius:20px;font-size:12px;font-weight:400;text-transform:uppercase;display:flex;align-items:center;justify-content:center}
</style>
</head>
<body>

<header class="abs nav">
  <div class="brand" style="left:111px;top:19px;width:193px;height:43px"><i></i>ReviewCodeHub</div>
  <nav class="abs nav-links">
    <span class="active">Home</span><span>Why trust me</span><span>Testimonials</span><span>FAQs</span><span>Contact us</span>
  </nav>
  <div class="btn-outline" style="left:952px;top:24px;width:136px;height:34px">Audit me now</div>
</header>

<section class="abs hero">
  <div class="hero-photo" role="img" aria-label="Photo of two consultants in an office, one with a coffee cup and one holding a notebook"></div>
  <div class="hero-blob"></div>
  <h1><span class="red">Is your Laravel App Slow,</span> Outdated Or Full Of Bugs?</h1>
  <p>Book a free Laravel code audit and get actionable insights in just 30 minutes.</p>
  <div class="hero-form"><span>Enter email address</span></div>
  <div class="btn-solid" style="left:252px;top:280px;width:222px;height:39px">Schedule free consultation</div>
  <div class="btn-outline" style="left:54px;top:348px;width:170px;height:40px;font-size:12px">Free consultancy</div>
</section>

<section class="struggle">
  <div class="abs struggle-frame"></div>
  <div class="abs struggle-photo" role="img" aria-label="Photo of a developer and a client reviewing code on a tablet at a desk"></div>
  <h2><span class="red">Are you struggling</span> with any of these?</h2>
  <ul class="checklist">
    <li><svg width="14" height="14" viewBox="0 0 14 14"><circle cx="7" cy="7" r="6" fill="none" stroke="#ff2314" stroke-width="1.4"/><path d="M4 7l2 2 5-5" fill="none" stroke="#ff2314" stroke-width="1.4"/></svg>Upgrading PHP / Laravel</li>
    <li><svg width="14" height="14" viewBox="0 0 14 14"><circle cx="7" cy="7" r="6" fill="none" stroke="#ff2314" stroke-width="1.4"/><path d="M4 7l2 2 5-5" fill="none" stroke="#ff2314" stroke-width="1.4"/></svg>No automated tests</li>
    <li><svg width="14" height="14" viewBox="0 0 14 14"><circle cx="7" cy="7" r="6" fill="none" stroke="#ff2314" stroke-width="1.4"/><path d="M4 7l2 2 5-5" fill="none" stroke="#ff2314" stroke-width="1.4"/></svg>Recurring bugs</li>
    <li><svg width="14" height="14" viewBox="0 0 14 14"><circle cx="7" cy="7" r="6" fill="none" stroke="#ff2314" stroke-width="1.4"/><path d="M4 7l2 2 5-5" fill="none" stroke="#ff2314" stroke-width="1.4"/></svg>Security issues</li>
    <li><svg width="14" height="14" viewBox="0 0 14 14"><circle cx="7" cy="7" r="6" fill="none" stroke="#ff2314" stroke-width="1.4"/><path d="M4 7l2 2 5-5" fill="none" stroke="#ff2314" stroke-width="1.4"/></svg>Slow performance</li>
    <li><svg width="14" height="14" viewBox="0 0 14 14"><circle cx="7" cy="7" r="6" fill="none" stroke="#ff2314" stroke-width="1.4"/><path d="M4 7l2 2 5-5" fill="none" stroke="#ff2314" stroke-width="1.4"/></svg>Messy architecture or no clear structure</li>
    <li><svg width="14" height="14" viewBox="0 0 14 14"><circle cx="7" cy="7" r="6" fill="none" stroke="#ff2314" stroke-width="1.4"/><path d="M4 7l2 2 5-5" fill="none" stroke="#ff2314" stroke-width="1.4"/></svg>Outdated packages / dependencies</li>
  </ul>
</section>

<section class="abs audit">
  <h2><span class="red">What You Get With a</span> Free Audit</h2>
  <div class="cards">
    <div class="card">
      <svg width="64" height="64" viewBox="0 0 64 64" fill="none" stroke="#ff2314" stroke-width="2"><circle cx="26" cy="24" r="20"/><circle cx="26" cy="20" r="6"/><rect x="32" y="34" width="28" height="24" rx="3"/><path d="M37 42h18M37 48h18M37 54h12"/></svg>
      A personalized code<br>review or system<br>analysis
    </div>
    <div class="card on">
      <svg width="64" height="64" viewBox="0 0 64 64" fill="none" stroke="#ffffff" stroke-width="2"><path d="M6 12h40v44H6z"/><path d="M14 46l10-14 8 8 10-16"/><path d="M44 6l12 12-18 18-8 2 2-8z"/></svg>
      Architecture &amp;<br>performance<br>insights
    </div>
    <div class="card">
      <svg width="64" height="64" viewBox="0 0 64 64" fill="none" stroke="#ff2314" stroke-width="2"><circle cx="32" cy="18" r="10"/><path d="M27 18l4 4 7-7"/><path d="M6 40l12-8 10 6 6-4 12 2 12 8-14 12-12-6-12 4z"/></svg>
      No commitment,<br>no spam
    </div>
    <div class="card">
      <svg width="64" height="64" viewBox="0 0 64 64" fill="none" stroke="#ff2314" stroke-width="2"><circle cx="32" cy="38" r="12"/><path d="M27 38l4 4 7-7"/><path d="M24 48l-4 12 12-5 12 5-4-12"/><path d="M32 4l2 4 4 1-3 3 1 4-4-2-4 2 1-4-3-3 4-1z"/></svg>
      +12 years of<br>Laravel<br>experience
    </div>
    <div class="card">
      <svg width="64" height="64" viewBox="0 0 64 64" fill="none" stroke="#ff2314" stroke-width="2"><rect x="6" y="6" width="52" height="44" rx="3"/><path d="M6 18h52M14 28h36M14 36h28M14 44h20"/><path d="M48 40l10-10 4 4-10 10-6 2z"/></svg>
      Delivered via a<br>video call or written<br>feedback
    </div>
  </div>
</section>

<section class="trust">
  <h2><span class="red">Why Trust</span> Me</h2>
  <p>Lorem ipsum dolor sit amet, consectetur adipiscing elit, sed do eiusmod tempor incididunt ut labore et dolore magna aliqua enim ad minim veniam, quis nostrud exercitation ullamco laboris nisi ut aliquip.</p>
  <ul class="links">
    <li><i style="background:#3a6cf4"></i>CodeVault</li>
    <li><i style="background:#111111"></i>Scribely</li>
    <li><i style="background:#3fa34d"></i>Open Source contributions</li>
  </ul>
  <div class="btn-outline" style="left:112px;top:2073px;width:334px;height:40px">Schedule a 30-mins free consultancy</div>
  <div class="abs trust-frame"></div>
  <div class="abs trust-photo" role="img" aria-label="Portrait photo of the Laravel consultant"></div>
  <div class="abs badge"><strong>12+</strong>YEARS OF<br>EXPERIENCE<br>WITH LARAVEL</div>
</section>

<div class="abs arrow" style="left:34px;top:2214px"><svg width="10" height="12" viewBox="0 0 10 12"><path d="M7 1L2 6l5 5" fill="none" stroke="#222" stroke-width="1.5"/></svg></div>
<div class="abs partners">
  <div class="partner"><i></i>Peoplewave</div>
  <div class="partner"><i></i>Createra</div>
  <div class="partner"><i></i>Northpoint</div>
  <div class="partner"><i></i>Brandly</div>
  <div class="partner"><i></i>Greenleaf</div>
</div>
<div class="abs arrow" style="left:1129px;top:2214px"><svg width="10" height="12" viewBox="0 0 10 12"><path d="M3 1l5 5-5 5" fill="none" stroke="#222" stroke-width="1.5"/></svg></div>

<section class="abs cta">
  <h2><span class="red">Let’s fix your Laravel headaches<br>together</span> – for free.</h2>
  <div class="btn-outline" style="left:900px;top:68px;width:188px;height:40px">Book my free call</div>
</section>

<h2 class="abs testi-title"><span class="red">Our</span> Testimonials</h2>
<article class="testi" style="left:93px">
  <div class="avatar" role="img" aria-label="Client headshot"></div>
  <div class="stars">★★★★★</div>
  <h3>Sarah H</h3>
  <p>“Lorem ipsum dolor sit amet, consectetur adipiscing elit, sed do eiusmod tempor incididunt ut labore et dolore.”</p>
</article>
<article class="testi on" style="left:442px">
  <div class="avatar" role="img" aria-label="Client headshot"></div>
  <div class="stars">★★★★★</div>
  <h3>Emily R</h3>
  <p>“Tobías helped us restructure our legacy Laravel codebase in a week. Highly recommended!”</p>
</article>
<article class="testi" style="left:792px">
  <div class="avatar" role="img" aria-label="Client couple photo"></div>
  <div class="stars">★★★★★</div>
  <h3>Mike and Jessica W</h3>
  <p>“Lorem ipsum dolor sit amet, consectetur adipiscing elit, sed do eiusmod tempor incididunt ut labore et dolore.”</p>
</article>

<h2 class="abs faq-title"><span class="red">Frequently Asked</span> Questions</h2>
<div class="faq" style="left:127px;top:3182px">What happens after I submit my email?<span class="plus">+</span></div>
<div class="faq" style="left:641px;top:3182px">Is the consultancy really free?<span class="plus">+</span></div>
<div class="faq" style="left:127px;top:3269px">What kind of projects do you work with?<span class="plus">+</span></div>
<div class="faq" style="left:641px;top:3269px">How long does the call last?<span class="plus">+</span></div>
<div class="faq" style="left:127px;top:3356px">Lorem ipsum dolor sit amet, consectetur?<span class="plus">+</span></div>
<div class="faq" style="left:641px;top:3356px">Lorem ipsum dolor sit amet, consectetur?<span class="plus">+</span></div>

<footer class="abs footer">
  <div class="brand" style="left:111px;top:49px;width:193px;height:43px"><i></i>ReviewCodeHub</div>
  <div class="btn-solid" style="left:453px;top:52px;width:210px;height:37px">Schedule consultation</div>
  <div class="btn-foot" style="left:679px;top:52px;width:169px;height:37px">Hire my services</div>
  <div class="btn-foot" style="left:863px;top:52px;width:225px;height:37px">hello@reviewcodehub.com</div>
  <div class="rule"></div>
  <div class="copy">©2025 Copyrights - All rights reserved</div>
  <div class="socials" aria-label="Social profiles"><i></i><i></i><i></i><i></i><i></i></div>
</footer>

</body>
</html>
```